Flyer-Design für meine Tätigkeit als freier Trauerredner
Zielgruppe
Für meine Tatigkeit als freier Trauerredner bei Beerdigungen möchte ich einen Flyer designen lassen, um diesen bei Bestattern aufzulegen sowie diese grundsätzlich als Informationsmaterial an interessierte Personen weitergeben zu können. Zielgruppe sind einerseits Personen, die sich lange im Vorfeld Gedanken über den Tod machen und den Wunsch äußern, im Rahmen einer persönlichen Gedenkfeier, unabhängig einer Konfessionszugehörigkeit und der Kirche verabschiedet zu werden. Auf der anderen Seite ist der Flyer ebenso für trauendernde Angehörige gedacht, die aufgrund eines unerwarteten Todesfalls sich mit dem Thema Beerdigung auseinadersetzen müssen und nach Alternativen zu einer krichlichen Beerdiugung suchen.
Aufgabenstellung
Eine Visitenkarte scheint mir im Format zu klein ... ein Flyer in einem größeren Format scheint mir geeigneter, Informationen zu vermitteln. Eine große Stärke von mir ist meine Emapthie. Der Flyer soll dies in der Bildsprache ausdrücken. Ebenso soll der Flyer durch die Bilder und die gewählte Sprahce Vertrauen aufbauen. Tod und Beerdigung sind für viele ein Tabuthemen ... der Flyer soll hier eine Brücke schlagen.
Wichtig wäre mir den Ablauf der Vorbereitung im Flyer aufzuskizzieren, um zu wissen, wie die Vorbereitung und Druchführung beispielhaft erfolgt.
Meine Kernaussage:
Freie Trauerreden, so einzigartig und besonders wie jeder Mensch selbst!
Als freier Trauerredner ist es mein Anspruch, den schweren Moment des Abschiednehmens so persönlich und würdevoll wie nur möglich zu gestalten!
Mein Ziel: Herzensverbindungen zwischen Menschen aufleben zu lassen und diese zu stärken. Herzensverbindungen leben und wirken weiter – unabhängig ob im Leben oder über den Tod hinaus!
Alle Informationen, die im Flyer aufgeführt werden sollen, sind dem beigefügten Word-Dokument zu entnehmen.
Wichtige Information finden Sie auf meiner Website www.tobiaskrämer.com
Wenn ein Statement oder Reszession benötigt wird und sich gut im Flyer macht, liefere ich diese gerne nach.

```html
<!DOCTYPE html>
<html lang="de">
<head>
<meta charset="utf-8">
<title>Freie Gedenkfeiern – Flyer</title>
<link rel="stylesheet" href="https://fonts.googleapis.com/css2?family=Arimo:wght@400;700&family=EB+Garamond:wght@400&display=swap">
<style>
  :root {
    --paper: #ffffff;
    --ink: #1a1a1a;
    --rule: #555555;
    --heart: #000000;
    --heart-text: #ffffff;
    --garden-light: #f3e3c2;
    --garden-mid: #9c8a5e;
    --garden-dark: #4f4a2a;
    --gate-light: #fbf3e6;
    --gate-mid: #c9b79c;
    --gate-dark: #7d6a55;
  }
  * { margin: 0; padding: 0; box-sizing: border-box; }
  html, body { width: 1200px; height: 600px; overflow: hidden; background: var(--paper); }
  .flyer {
    position: relative; width: 1200px; height: 600px; overflow: hidden;
    font-family: "Arimo", Arial, sans-serif; color: var(--ink);
    font-size: 7.8px; line-height: 9.68px;
  }
  .frame { position: absolute; left: 24px; top: 22px; width: 1152px; height: 555px; border: 0.6px solid var(--rule); }
  .photo-garden {
    position: absolute; left: 632px; top: 0; width: 513px; height: 321px;
    background:
      radial-gradient(ellipse 30% 40% at 62% 20%, #fffaf0 0%, rgba(255,245,220,0.8) 35%, rgba(255,240,210,0) 70%),
      linear-gradient(180deg, var(--garden-light) 0%, #cdb78f 45%, var(--garden-mid) 65%, var(--garden-dark) 100%);
  }
  .photo-gate {
    position: absolute; left: 0; top: 199px; width: 225px; height: 346px;
    background:
      radial-gradient(ellipse 45% 35% at 45% 30%, #ffffff 0%, rgba(255,250,240,0.9) 40%, rgba(255,250,240,0) 75%),
      linear-gradient(90deg, var(--gate-dark) 0%, var(--gate-mid) 30%, var(--gate-light) 55%, var(--gate-mid) 80%, var(--gate-dark) 100%);
  }
  .headline {
    position: absolute; left: 63px; top: 52px;
    font-family: "EB Garamond", Georgia, serif; font-weight: 400;
    font-size: 20px; line-height: 24.2px; letter-spacing: 0.4px; text-transform: uppercase;
  }
  .intro { position: absolute; left: 63px; top: 135px; width: 380px; }
  .heart { position: absolute; left: 436px; top: 68px; width: 92px; height: 77px; }
  .heart-text {
    position: absolute; left: 436px; top: 85px; width: 92px;
    color: var(--heart-text); text-align: center; font-size: 7.6px; line-height: 9.7px;
  }
  .section-title {
    position: absolute; font-family: "EB Garamond", Georgia, serif; font-weight: 400;
    font-size: 16px; line-height: 18px; letter-spacing: 0.5px; text-transform: uppercase; white-space: pre;
  }
  .column { position: absolute; }
  .column h3 { font-size: 7.8px; line-height: 9.68px; font-weight: 700; }
  .column p { margin-bottom: 9.68px; }
  .column ul { list-style: none; margin-bottom: 9.68px; }
  .column li { padding-left: 11px; text-indent: -4.5px; }
  .column li::before { content: "• "; }
  .col-info { left: 259px; top: 229px; width: 308px; }
  .col-prep { left: 636px; top: 384px; width: 252px; }
  .col-flow { left: 906px; top: 379px; width: 248px; }
</style>
</head>
<body>
<main class="flyer">
  <div class="frame"></div>
  <div class="photo-garden" role="img" aria-label="Sonnendurchfluteter Garten mit Baumhaus, kahlen Bäumen und hellen Stoffbändern im Gegenlicht"></div>
  <div class="photo-gate" role="img" aria-label="Offenes Holztor mit Kiesweg, durch das helles Licht fällt"></div>

  <h1 class="headline">Freie Gedenkfeiern,<br>so einzigartig und besonders<br>wie jeder Mensch selbst!</h1>
  <p class="intro">Mein Ziel ist es, Herzensverbindungen zwischen Menschen aufleben zu lassen und zu stärken.<br>Herzensverbindungen leben und wirken weiter – unabhängig ob im Leben oder über den Tod hinaus!</p>

  <svg class="heart" viewBox="0 0 92 77" aria-hidden="true">
    <path fill="var(--heart)" d="M46 77 C30 63 0 45 0 22 C0 9 10 0 23 0 C34 0 42 6 46 13 C50 6 58 0 69 0 C82 0 92 9 92 22 C92 45 62 63 46 77 Z"/>
  </svg>
  <p class="heart-text">Kostenfreies Infor-<br>mationsgespräch<br>mit Tobias Krämer<br>vereinbaren</p>

  <h2 class="section-title" style="left:259px; top:198px;">Allgemeine   Informationen</h2>
  <section class="column col-info">
    <h3>Was ist eine freie Trauerfeier/Gedenkfeier?</h3>
    <p>Freie Trauerzeremonie, Gedenkfeier, Beerdigung, Lebensabschiedsfeier… Synonyme für eine, von mir als freier Trauerredner durchgeführte, Abschiedszeremonie, die ganz individuell und persönlich auf die verstorbene Person oder das verstorbene Kind bezogen ist - weltlich frei, unabhängig einer Konfession mit individuellem Ablauf.</p>
    <h3>Orte für freie Trauerfeiern</h3>
    <p>Freie Trauerfeiern finden meist auf Friedhöfen, in Kapellen oder Aussegnungshallen, auf dem Friedhofsgelände, einem Waldfriedhof oder auch in den eigenen Räumen des Bestatters statt. Auch ein selbstgewählter Ort in der Natur kann unter bestimmten Voraussetzungen möglich sein.</p>
    <h3>Dauer einer freien Traufeier</h3>
    <p>Eine freie Trauerfeier dauert in der Regel 20 - 30 Minuten.</p>
    <h3>Kosten der Trauerrede / Gedenkfeier</h3>
    <p>Die Kosten für die Trauerrede, bzw. der Umrahmung Gedenkfeier betragen 439 EUR inkl. MwSt. Die Pauschale beinhaltet das Vorbereitungsgespräch sowie die Aufbereitung und Durchführung der freien Trauerrede, die Sie zum Nachlesen als persönliches Exemplar erhalten. Die Fahrtkosten betragen 55 Cent je Kilometer für die Fahrt zum Friedhof bzw. Ort der Verabschiedung und zurück.</p>
    <h3>Eine freie Trauerzeremonie beinhaltet<br>im Wesentlichen folgenden Elemente:</h3>
    <ul>
      <li>Gedenken an die verstorbene Person in einem feierlichen Rahmen</li>
      <li>Herausstellen der einzigartigen Persönlichkeit und den Charakter der Person – würdevoll wird dies in den Mittelpunkt der Feier gestellt</li>
      <li>Aufleben lassen wertvoller Erinnerungen und Ausdruck der Dankbarkeit an die gemeinsamen Stunden und damit Stärkung der Herzensverbindung</li>
      <li>der Trauer Raum zu geben und die freie Trauerfeier Bestandteil des Aufarbeitungsprozesses werden zu lassen</li>
      <li>Beistand, Trost und Zuspruch erfahren - durch die anwesenden Trauergäste, den freien Trauerredner, alles Verbindende und/ oder das Göttliche</li>
    </ul>
  </section>

  <h2 class="section-title" style="left:636px; top:358px;">Vorbereitung / Ablauf</h2>
  <section class="column col-prep">
    <p>Lichtvolle - würdevolle - persönliche Wege des Abschieds – Vorbereitung und Ablauf. Detailinformationen zu den einzelnen Punkten finden Sie im Internet unter www.tobiaskrämer.com</p>
    <h3>ÜBERLEGUNGEN IM VORFELD:</h3>
    <p style="margin-bottom:0">Es ist gut, im ersten Schritt der Planung einer freien Trauerfeier grundsätzlichen Überlegungen Raum zu geben, wie zum Beispiel:</p>
    <ul>
      <li>Hat die/der Verstorbene im Vorfeld Wünsche zur eigenen Beerdigung geäußert?</li>
      <li>Wie sollte die freie Trauerfeier ablaufen, damit die Gedenkfeier „stimmig“ ist – für die verstorbene Person, Sie selbst, Familie, Freunde und sie diese später in guter Erinnerung behalten?</li>
    </ul>
    <h3>DAS VORBEREITUNGSGESPRÄCH – Dauer ca. 2 Stunden</h3>
    <p>Persönlich, telefonisch oder digital werden in einem Vorbereitungsgespräch alle wichtigen Informationen zur verstorbenen Person gesammelt und gemeinsam der Ablauf der freien Gedenkfeier geplant.</p>
  </section>

  <section class="column col-flow">
    <h3>Ablauf der Gedenkfeier – Dauer ca. 20 – 30 Minuten</h3>
    <p>Den Möglichkeiten des Ablaufs einer freien Trauerfeier sind wenig Grenzen gesetzt – ihre Bedürfnisse und Wünsche stehen im Mittelpunkt!</p>
    <h3>Wichtige Elemente:</h3>
    <ul>
      <li>Persönliche Worte in Form einer individuellen Trauerrede zur Würdigung des Lebens der verstorbenen Person</li>
      <li>Ausgewählte Musikstücke</li>
      <li>Aktive Beteiligung Ihrerseits, von Angehörigen und/oder Freunden durch das Vorlesen eines Gedichts, eines Gebets oder persönlich verfasster Worte</li>
      <li>Rituale des Gedenkens können einen würdevollen, persönlichen Beitrag umrahmen und in verschiedenster Weise integriert werden, z.B. Seifenblasen, Briefe/Wünsche, eine Lichterkranz der Verbundenheit oder Wunderkerzen zum Schluss einer Gedenkfeier, um symbolisch Sterne der Liebe und Dankbarkeit regnen zu lassen…</li>
    </ul>
  </section>
</main>
</body>
</html>
```